Your complete Gardening and lawn maintenance, Horticultural care. (to be on card)
We are looking at using a logo of a tree, with a recycling emblem circling the tree. The colors of choice, are burnt oranges and olive greens. Presented; simple to the eye, yet catchy to the clients in a eco-friendly way. We have uploaded a design for you to look at just to give a rough idea, you can use that or create your own ideas or play around with a mixture.

Target Market(s)

Home owners, businesses, real estates.

Industry/Entity Type

Recycling

Contact Information for Business Card

Name: Colin Breversted
Phone: 0438159027
Email: brightmossyards@mailbarn.net

Logo Text

Bright-Moss Yards

Logo styles of interest
Emblem Logo
Pictorial/Combination Logo
Abstract Logo
Requirements
Must have
• Business name: Bright-Moss Yards
and slogan : Your complete Gardening and lawn maintenance, Horticultural care

```html
<!DOCTYPE html>
<html lang="en">
<head>
<meta charset="utf-8">
<title>Bright-Moss Yards – Business Card</title>
<link rel="stylesheet" href="https://fonts.googleapis.com/css2?family=Alegreya:wght@400&family=Arimo:wght@700&display=swap">
<style>
  :root {
    --paper: #ffffff;
    --frame: #3a3a3a;
    --olive: #5a6e23;
    --olive-light: #a3b44a;
    --maroon: #4a1a1e;
  }
  html, body {
    margin: 0;
    padding: 0;
    width: 1200px;
    height: 703px;
    overflow: hidden;
    background: var(--paper);
  }
  .card {
    position: relative;
    width: 1200px;
    height: 703px;
    background: var(--paper);
  }
  .card-frame {
    position: absolute;
    left: 33px;
    top: 31px;
    width: 1133px;
    height: 636px;
    border: 1px solid var(--frame);
    box-sizing: border-box;
  }
  .brand-dot {
    position: absolute;
    left: 110px;
    top: 100px;
    width: 370px;
    height: 370px;
    border-radius: 50%;
    background: var(--olive-light);
  }
  .brand-name {
    position: absolute;
    left: 530px;
    top: 118px;
    margin: 0;
    font-family: "Arimo", Arial, sans-serif;
    font-weight: 700;
    font-size: 80px;
    line-height: 96px;
    color: var(--olive);
  }
  .tagline {
    position: absolute;
    right: 138px;
    top: 308px;
    margin: 0;
    font-family: "Alegreya", Georgia, serif;
    font-size: 28px;
    line-height: 36px;
    color: var(--maroon);
    text-align: right;
  }
  .person-name {
    position: absolute;
    left: 539px;
    top: 442px;
    margin: 0;
    font-family: "Arimo", Arial, sans-serif;
    font-weight: 700;
    font-size: 32px;
    color: var(--olive);
  }
  .person-name .surname { color: var(--olive-light); }
  .contact-line {
    position: absolute;
    left: 121px;
    top: 583px;
    margin: 0;
    font-family: "Arimo", Arial, sans-serif;
    font-weight: 700;
    font-size: 29px;
    color: var(--maroon);
    white-space: nowrap;
  }
  .contact-line .label { color: var(--olive); }
  .contact-line .contact-item + .contact-item { margin-left: 36px; }
</style>
</head>
<body>
  <main class="card">
    <div class="card-frame"></div>
    <div class="brand-dot"></div>
    <h1 class="brand-name">Bright-Moss<br>Yards</h1>
    <p class="tagline">Your complete Gardening and<br>Lawn Maintenance, Horticulture Care</p>
    <p class="person-name">Colin <span class="surname">Breversted</span></p>
    <p class="contact-line">
      <span class="contact-item"><span class="label">Tel:</span> 043 815 9027</span><span class="contact-item"><span class="label">Email:</span> brightmossyards@mailbarn.net</span>
    </p>
  </main>
</body>
</html>
```